Darin Wekel Orthodontics
Business Card, Letterhead, Envelopes, Folder
@ Project holder : Please,Extend this Contest.
I am interested and Coming....
Anyone do a full size envelope where the letterhead slides in the envelope unfolded.
Anyone willing to experiment by putting the log and info at the bottom of the stationary page rather than the top.
Thanks for your submissions.#2,3,6,7 appear too busy for me. Lets stick with simplicity. Back of business card should probably have a white or light background so we can write the appoitment time in pen on the card.
ai format uploaded
kindly upload ai or eps file of logo

```html
<!DOCTYPE html>
<html lang="en">
<head>
<meta charset="utf-8">
<title>Darin Wekel Orthodontics — Stationery</title>
<link rel="stylesheet" href="https://fonts.googleapis.com/css2?family=Montserrat:wght@300;400;600&display=swap">
<style>
  :root {
    --navy: #0f2f6b;
    --blue: #1f4f9c;
    --blue-mid: #3a6fc0;
    --blue-light: #8fb0e0;
    --paper: #ffffff;
    --ink: #243a63;
    --muted: #7f8aa3;
    --ghost: #dfe3ec;
    --stage: #e9ebef;
  }
  * { margin: 0; padding: 0; box-sizing: border-box; }
  html, body { width: 1200px; height: 750px; overflow: hidden; }
  body {
    background: var(--stage);
    font-family: "Montserrat", sans-serif;
    color: var(--ink);
    position: relative;
  }
  .sheet {
    position: absolute;
    background: var(--paper);
    overflow: hidden;
    box-shadow: 0 3px 10px rgba(15, 30, 60, 0.18);
  }
  .swoosh { position: absolute; inset: 0; width: 100%; height: 100%; }
  .wordmark { position: absolute; font-weight: 300; line-height: 1.05; }
  .wordmark .sub { display: block; font-size: 0.42em; letter-spacing: 0.12em; }

  /* Business card front */
  .card-front { left: 120px; top: 96px; width: 264px; height: 132px; }
  .card-front .wordmark { right: 14px; top: 14px; font-size: 17px; color: var(--navy); text-align: right; }
  .card-front .details {
    position: absolute; right: 14px; bottom: 14px; text-align: right;
    font-size: 6.5px; line-height: 1.45; color: var(--ink);
  }
  .card-front .details b { font-weight: 600; }

  /* Business card back */
  .card-back { left: 396px; top: 96px; width: 269px; height: 132px; padding: 14px 16px; }
  .card-back .wordmark { left: 16px; top: 12px; font-size: 13px; color: var(--navy); }
  .card-back .web { position: absolute; right: 16px; top: 16px; font-size: 6.5px; color: var(--blue-mid); }
  .card-back .appt { position: absolute; left: 16px; right: 16px; top: 48px; }
  .card-back .line {
    display: flex; align-items: flex-end; gap: 6px;
    font-size: 7px; color: var(--blue-mid); height: 18px;
  }
  .card-back .line span.rule { flex: 1; border-bottom: 1px solid var(--blue-light); }
  .card-back .note {
    position: absolute; left: 0; right: 0; bottom: 10px; text-align: center;
    font-size: 5.5px; color: var(--muted);
  }

  /* Envelope */
  .envelope { left: 72px; top: 312px; width: 581px; height: 360px; }
  .envelope .flap-edge {
    position: absolute; left: 0; right: 0; top: 0; height: 72px;
    border-bottom: 1px solid rgba(255, 255, 255, 0.25);
    border-radius: 0 0 40px 40px;
  }
  .envelope .wordmark { left: 26px; top: 92px; font-size: 30px; color: var(--paper); }
  .envelope .address {
    position: absolute; right: 30px; bottom: 26px; text-align: right;
    font-size: 9px; line-height: 1.55; color: var(--ink);
  }
  .envelope .address b { font-weight: 600; }

  /* Letterhead */
  .letterhead { left: 679px; top: 77px; width: 425px; height: 607px; }
  .letterhead .swoosh { height: 118px; }
  .letterhead .wordmark { right: 22px; top: 22px; font-size: 26px; color: var(--paper); text-align: right; }
  .letterhead .ghost-name {
    position: absolute; left: 0; right: 0; top: 270px; text-align: center;
    font-weight: 300; font-size: 60px; color: var(--ghost);
  }
  .letterhead .footer {
    position: absolute; left: 0; right: 0; bottom: 26px; text-align: center;
    font-size: 8px; line-height: 1.6; color: var(--muted);
  }
</style>
</head>
<body>

<section class="sheet card-front" aria-label="Business card front">
  <svg class="swoosh" viewBox="0 0 264 132" preserveAspectRatio="none" aria-hidden="true">
    <defs>
      <linearGradient id="cardBlue" x1="0" y1="0" x2="1" y2="1">
        <stop offset="0" stop-color="#0f2f6b"/>
        <stop offset="1" stop-color="#2c5fb0"/>
      </linearGradient>
    </defs>
    <path d="M0 0 H150 C110 30 70 80 55 132 H0 Z" fill="url(#cardBlue)"/>
    <path d="M150 0 C110 30 70 80 55 132" stroke="#fff" stroke-width="5" fill="none"/>
    <path d="M120 0 C88 32 58 80 44 132" stroke="#fff" stroke-width="3" fill="none" opacity="0.9"/>
    <path d="M95 0 C68 34 44 82 33 132" stroke="#8fb0e0" stroke-width="2" fill="none" opacity="0.8"/>
    <path d="M170 0 C128 34 90 84 76 132" stroke="#3a6fc0" stroke-width="3" fill="none" opacity="0.6"/>
  </svg>
  <div class="wordmark">Darin Wekel<span class="sub">ORTHODONTICS</span></div>
  <div class="details">
    Darin Wekel, DDS<br>
    Suite 210, 118 Maple Ridge Road NW<br>
    Calgary, Alberta T2K 4R8<br>
    <b>Phone:</b> 403 555-0182<br>
    <b>Email:</b> info@darinwekelortho.ca
  </div>
</section>

<section class="sheet card-back" aria-label="Business card back">
  <div class="wordmark">Darin Wekel<span class="sub">ORTHODONTICS</span></div>
  <div class="web">www.darinwekelortho.ca</div>
  <div class="appt">
    <div class="line">Your next appointment: <span class="rule"></span></div>
    <div class="line">Date / time: <span class="rule"></span></div>
    <div class="line">Date / time: <span class="rule"></span></div>
  </div>
  <div class="note">Please give 24 hours notice for any changes to your appointment.</div>
</section>

<section class="sheet envelope" aria-label="Envelope">
  <svg class="swoosh" viewBox="0 0 581 360" preserveAspectRatio="none" aria-hidden="true">
    <defs>
      <linearGradient id="envBlue" x1="0" y1="0" x2="1" y2="1">
        <stop offset="0" stop-color="#0f2f6b"/>
        <stop offset="0.6" stop-color="#1f4f9c"/>
        <stop offset="1" stop-color="#3a6fc0"/>
      </linearGradient>
    </defs>
    <path d="M0 0 H581 V60 C400 90 170 170 0 330 Z" fill="url(#envBlue)"/>
    <path d="M581 60 C400 90 170 170 0 330" stroke="#fff" stroke-width="10" fill="none"/>
    <path d="M581 30 C390 62 160 140 0 290" stroke="#fff" stroke-width="5" fill="none" opacity="0.85"/>
    <path d="M581 90 C410 120 200 200 40 360" stroke="#3a6fc0" stroke-width="6" fill="none" opacity="0.55"/>
    <path d="M581 120 C430 150 240 225 110 360" stroke="#8fb0e0" stroke-width="3" fill="none" opacity="0.5"/>
  </svg>
  <div class="flap-edge"></div>
  <div class="wordmark">Darin Wekel<span class="sub">ORTHODONTICS</span></div>
  <div class="address">
    Suite 210<br>
    118 Maple Ridge Road NW<br>
    Calgary, Alberta T2K 4R8<br>
    <b>Phone:</b> 403 555-0182<br>
    <b>Email:</b> info@darinwekelortho.ca
  </div>
</section>

<section class="sheet letterhead" aria-label="Letterhead">
  <svg class="swoosh" viewBox="0 0 425 118" preserveAspectRatio="none" aria-hidden="true">
    <defs>
      <linearGradient id="lhBlue" x1="0" y1="0" x2="1" y2="0">
        <stop offset="0" stop-color="#3a6fc0"/>
        <stop offset="0.5" stop-color="#1f4f9c"/>
        <stop offset="1" stop-color="#0f2f6b"/>
      </linearGradient>
    </defs>
    <path d="M0 0 H425 V110 C300 60 140 40 0 55 Z" fill="url(#lhBlue)"/>
    <path d="M0 55 C140 40 300 60 425 110" stroke="#fff" stroke-width="5" fill="none"/>
    <path d="M0 40 C150 24 300 44 425 92" stroke="#fff" stroke-width="3" fill="none" opacity="0.85"/>
    <path d="M0 70 C140 56 290 74 425 118" stroke="#8fb0e0" stroke-width="3" fill="none" opacity="0.7"/>
  </svg>
  <div class="wordmark">Darin Wekel<span class="sub">ORTHODONTICS</span></div>
  <div class="ghost-name" aria-hidden="true">Darin Wekel</div>
  <div class="footer">
    Suite 210, 118 Maple Ridge Road NW, Calgary, Alberta T2K 4R8<br>
    Phone: 403 555-0182 | Email: info@darinwekelortho.ca
  </div>
</section>

</body>
</html>
```